Deliverables
1) Business Card (double sided)
2) Letterhead
3) Compliment Slip
4) Single Page A4 / A5 Brochure / Flyer
We require a very professional looking stationary set to include: letterhead, compliments slip and business cards (double sided bus cards).
All deliverables should seek to have a clean crisp corporate layout and theme to them, incorporating the logo (files attached).
All files should be in adobe illustrator, photoshop. The letterhead should ideally be in MS Word.
For the A4 / A5 flyer I'm looking for a template which I can look to add various marketing campaigns into the primary being IT Support, if its layout can incorporate the company logo, colour scheme, etc. If the initial template can have a layout where I can add a number of 'key points' to it.
Details - Company Address
Brindle 4
Harrowgate Business Centre
Dunmore Crescent
Northumberland
NE41 2QP
www.brindle-4.co.uk
enquiries@brindle-4.co.uk
T:01632 960 318
Details - Business Card
Dr. Malcolm J. Rudd
malcolm@brindle-4.co.uk
T:01632 960 318
M: 07700900841
Logo Information
Font - Aller
RGB #7D7D7D , #479EC9
CMYK (52,44,44,9) , (69,24,9,0)
Target Market(s)
SME Seeking IT Consultancy
Industry/Entity Type
Marketing
Requirements
Must have
- Incorporate company logo and colour schemem.

```html
<!DOCTYPE html>
<html lang="en">
<head>
<meta charset="utf-8">
<title>Brindle 4 – Stationery Set</title>
<link href="https://fonts.googleapis.com/css2?family=PT+Sans:wght@400;700&display=swap" rel="stylesheet">
<style>
  :root {
    --brand-blue: #479ec9;
    --brand-grey: #7d7d7d;
    --stage: #449dcb;
    --paper: #ffffff;
    --footer-grey: #7a7a7a;
    --shadow: 0 2px 6px rgba(0,0,0,0.35);
  }
  * { box-sizing: border-box; margin: 0; padding: 0; }
  html, body { width: 1200px; height: 900px; overflow: hidden; }
  body {
    background: var(--stage);
    font-family: "PT Sans", sans-serif;
    color: var(--brand-grey);
    position: relative;
  }
  .sheet { position: absolute; background: var(--paper); box-shadow: var(--shadow); overflow: hidden; }

  /* brand lockup: plain circle + name */
  .brand { position: absolute; display: flex; align-items: center; color: var(--brand-grey); font-weight: 400; white-space: nowrap; line-height: 1; }
  .brand-dot { border-radius: 50%; background: var(--brand-blue); flex: none; }
  .brand--white { color: #fff; }
  .brand--white .brand-dot { background: #fff; }

  .contact-list { position: absolute; list-style: none; font-weight: 700; font-size: 8.5px; color: var(--brand-grey); }
  .contact-list li { display: flex; align-items: center; gap: 4px; height: 13px; white-space: nowrap; }
  .tag { display: inline-flex; width: 10px; height: 10px; align-items: center; justify-content: center; color: #fff; font-size: 7px; font-weight: 700; flex: none; }
  .tag--blue { background: var(--brand-blue); }
  .tag--grey { background: var(--brand-grey); }

  /* Letterhead */
  .letterhead { left: 34px; top: 25px; width: 596px; height: 842px; }
  .letterhead .brand { left: 54px; top: 44px; font-size: 38px; }
  .letterhead .brand-dot { width: 38px; height: 38px; margin-right: 10px; }
  .letterhead .address { position: absolute; left: 42px; top: 102px; font-size: 8.5px; font-weight: 700; }
  .letterhead .rule { position: absolute; left: 42px; top: 124px; width: 510px; height: 2px; background: var(--brand-blue); }
  .letterhead .contact-list { left: 464px; top: 61px; }

  /* Business card back */
  .card-back { left: 49px; top: 188px; width: 242px; height: 157px; }
  .card-back .brand { left: 13px; top: 52px; font-size: 40px; }
  .card-back .brand-dot { width: 40px; height: 40px; margin-right: 12px; }
  .card-back .web { position: absolute; right: 14px; top: 96px; font-size: 9px; font-weight: 700; }

  /* Compliment slip */
  .comp-slip { left: 6px; top: 296px; width: 596px; height: 281px; }
  .comp-slip .brand { left: 360px; top: 38px; font-size: 36px; }
  .comp-slip .brand-dot { width: 34px; height: 34px; margin-right: 12px; }
  .comp-slip .heading { position: absolute; left: 43px; top: 192px; font-size: 12px; font-weight: 700; }
  .comp-slip .rule { position: absolute; left: 43px; top: 213px; width: 510px; height: 2px; background: var(--brand-blue); }
  .comp-slip .address { position: absolute; left: 43px; top: 221px; font-size: 7.5px; font-weight: 700; }
  .comp-slip .contact-list { left: 43px; top: 237px; display: flex; gap: 16px; }

  /* Business card front */
  .card-front { left: 162px; top: 571px; width: 242px; height: 157px; }
  .card-front .brand { left: 10px; top: 15px; font-size: 23px; }
  .card-front .brand-dot { width: 22px; height: 22px; margin-right: 7px; }
  .card-front .name { position: absolute; left: 0; right: 0; top: 64px; text-align: center; font-size: 13px; font-weight: 700; }
  .card-front .contact-list { left: 10px; top: 100px; font-size: 7.5px; }
  .card-front .contact-list li { height: 12px; }
  .card-front .address { position: absolute; right: 10px; top: 102px; text-align: right; font-size: 7.5px; font-weight: 700; line-height: 10px; font-style: normal; }

  /* A4 flyer */
  .flyer-a4 { left: 785px; top: 32px; width: 357px; height: 505px; }
  .flyer-a4 .frame { position: absolute; inset: 8px; border: 1.5px solid var(--brand-blue); }
  .flyer-a4 .band { position: absolute; left: 8px; top: 83px; width: 235px; height: 33px; background: var(--brand-blue); color: #fff; font-size: 15px; padding: 8px 0 0 8px; }
  .flyer-a4 .brand { left: 254px; top: 92px; font-size: 16px; }
  .flyer-a4 .brand-dot { width: 15px; height: 15px; margin-right: 5px; }
  .flyer-a4 .wave-art { position: absolute; left: 9px; top: 200px; width: 339px; height: 290px;
    background: linear-gradient(170deg, rgba(71,158,201,0) 0%, rgba(71,158,201,0.18) 40%, rgba(71,158,201,0.3) 65%, rgba(71,158,201,0.08) 100%); }

  /* A5 flyer */
  .flyer-a5 { left: 650px; top: 417px; width: 254px; height: 357px; }
  .flyer-a5 .header { position: absolute; left: 0; top: 0; width: 100%; height: 32px; background: var(--brand-blue); }
  .flyer-a5 .brand { right: 18px; top: 8px; font-size: 17px; }
  .flyer-a5 .brand-dot { width: 16px; height: 16px; margin-right: 5px; }
  .flyer-a5 .footer { position: absolute; left: 0; bottom: 0; width: 100%; height: 33px; background: var(--footer-grey); color: #fff; font-size: 5px; font-weight: 700; padding: 6px 0 0 4px; }
  .flyer-a5 .footer .contact-list { position: static; color: #fff; font-size: 5px; display: flex; gap: 8px; margin-top: 5px; }
  .flyer-a5 .footer .tag { width: 7px; height: 7px; font-size: 5px; background: #fff; color: var(--footer-grey); }
</style>
</head>
<body>

<section class="sheet letterhead" aria-label="Letterhead">
  <div class="brand"><span class="brand-dot"></span>Brindle 4</div>
  <p class="address">Harrowgate Business Centre, Northumberland, NE41 2QP</p>
  <ul class="contact-list">
    <li><span class="tag tag--blue">T</span>01632 960 318</li>
    <li><span class="tag tag--grey">M</span>07700 900 841</li>
    <li><span class="tag tag--blue">E</span>malcolm@brindle-4.co.uk</li>
    <li><span class="tag tag--grey">W</span>www.brindle-4.co.uk</li>
  </ul>
  <div class="rule"></div>
</section>

<section class="sheet card-back" aria-label="Business card back">
  <div class="brand"><span class="brand-dot"></span>Brindle 4</div>
  <p class="web">www.brindle-4.co.uk</p>
</section>

<section class="sheet comp-slip" aria-label="Compliment slip">
  <div class="brand"><span class="brand-dot"></span>Brindle 4</div>
  <h2 class="heading">With Compliments</h2>
  <div class="rule"></div>
  <p class="address">Brindle 4, Harrowgate Business Centre, Northumberland, NE41 2QP</p>
  <ul class="contact-list">
    <li><span class="tag tag--blue">T</span>01632 960 318</li>
    <li><span class="tag tag--grey">M</span>07700 900 841</li>
    <li><span class="tag tag--blue">E</span>malcolm@brindle-4.co.uk</li>
    <li><span class="tag tag--grey">W</span>www.brindle-4.co.uk</li>
  </ul>
</section>

<section class="sheet card-front" aria-label="Business card front">
  <div class="brand"><span class="brand-dot"></span>Brindle 4</div>
  <h2 class="name">Dr. Malcolm J. Rudd</h2>
  <ul class="contact-list">
    <li><span class="tag tag--blue">T</span>01632 960 318</li>
    <li><span class="tag tag--grey">M</span>07700 900 841</li>
    <li><span class="tag tag--blue">E</span>malcolm@brindle-4.co.uk</li>
    <li><span class="tag tag--grey">W</span>www.brindle-4.co.uk</li>
  </ul>
  <address class="address">Brindle 4<br>Harrowgate Business Centre<br>Dunmore Crescent<br>Northumberland<br>NE41 2QP</address>
</section>

<section class="sheet flyer-a4" aria-label="A4 flyer template">
  <div class="frame"></div>
  <div class="band">Managed IT Services</div>
  <div class="brand"><span class="brand-dot"></span>Brindle 4</div>
  <div class="wave-art" role="img" aria-label="Decorative flowing blue line wave pattern"></div>
</section>

<section class="sheet flyer-a5" aria-label="A5 flyer template">
  <div class="header">
    <div class="brand brand--white"><span class="brand-dot"></span>Brindle 4</div>
  </div>
  <div class="footer">
    <p>Brindle 4, Harrowgate Business Centre, Northumberland, NE41 2QP</p>
    <ul class="contact-list">
      <li><span class="tag">T</span>01632 960 318</li>
      <li><span class="tag">M</span>07700 900 841</li>
      <li><span class="tag">E</span>malcolm@brindle-4.co.uk</li>
      <li><span class="tag">W</span>www.brindle-4.co.uk</li>
    </ul>
  </div>
</section>

</body>
</html>
```